Healthy Supplement featuring Moringa products

Need 3 business card options for our reps to order from Printwell. Our reps will be ordering from Printwell once we upload them. Attached is our current designs to show what info needs to be on the cards. Our website is www.tqvitality.com
The business cards will be a template for our reps to order from. Most of our reps are Asian & Hispanic. Please look at our website so you can see who we are to get the look and feel what we need.
Target Market(s)
Adults 30 on up. Health oriented people.
Industry/Entity Type
Health And Wellness
Contact Information for Business Card
Name
Title
Phone
Logo
www.tqvitality.com/my/username
Font styles to use
Requirements
Must have
- Please match our website look and colors. A moringa leaf is nice, but am open to something different.
Nice to have
- Healthy looking and warm, not super cold or too modern.
Should not have
- No harsh colors please.

```html
<!DOCTYPE html>
<html lang="en">
<head>
<meta charset="utf-8">
<title>TQ Vitality – Business Card</title>
<link href="https://fonts.googleapis.com/css2?family=Marcellus&family=Open+Sans:wght@400;600&display=swap" rel="stylesheet">
<style>
  :root {
    --stage: #2c3034;
    --card: #ffffff;
    --leaf: #5a9f2a;
    --leaf-light: #8cc63f;
    --charcoal: #2f2f31;
    --ink: #2a2a2a;
  }
  html, body {
    margin: 0;
    width: 1200px;
    height: 900px;
    overflow: hidden;
    background: var(--stage);
  }
  .canvas {
    position: relative;
    width: 1200px;
    height: 900px;
  }
  .card {
    position: absolute;
    width: 560px;
    height: 320px;
    background: var(--card);
    border-radius: 22px;
    overflow: hidden;
    box-shadow: 0 10px 30px rgba(0,0,0,.35);
  }

  /* Front card */
  .card--front { left: 580px; top: 100px; }
  .front__brand {
    position: absolute;
    left: 0; right: 0;
    top: 92px;
    text-align: center;
    font-family: "Marcellus", serif;
    font-size: 54px;
    letter-spacing: 4px;
    color: var(--leaf);
  }
  .front__rule {
    position: absolute;
    left: 0; right: 0;
    top: 226px;
    height: 2px;
    background: var(--leaf-light);
  }
  .front__tab {
    position: absolute;
    left: 95px;
    top: 213px;
    height: 28px;
    padding: 0 18px;
    border-radius: 6px;
    background: var(--leaf-light);
    color: #fff;
    font-family: "Marcellus", serif;
    font-size: 14px;
    letter-spacing: 2px;
    line-height: 28px;
  }

  /* Back card */
  .card--back { left: 70px; top: 480px; }
  .back__art { position: absolute; inset: 0; }
  .back__name {
    position: absolute;
    left: 218px; top: 36px;
    font-family: "Marcellus", serif;
    font-size: 22px;
    letter-spacing: 1px;
    color: var(--ink);
  }
  .back__title {
    position: absolute;
    left: 218px; top: 64px;
    font-family: "Open Sans", sans-serif;
    font-size: 13px;
    font-weight: 600;
    color: var(--leaf);
  }
  .back__rule {
    position: absolute;
    left: 290px; right: 0;
    top: 74px;
    height: 2px;
    background: var(--leaf-light);
  }
  .contact {
    position: absolute;
    left: 212px; top: 98px;
    margin: 0; padding: 0;
    list-style: none;
    font-family: "Open Sans", sans-serif;
    font-size: 13px;
    color: var(--ink);
  }
  .contact__item {
    display: flex;
    align-items: center;
    gap: 9px;
    height: 24px;
  }
  .contact__icon { width: 15px; height: 15px; flex: none; }
  .back__brand {
    position: absolute;
    right: 34px; bottom: 36px;
    font-family: "Marcellus", serif;
    font-size: 30px;
    letter-spacing: 2px;
    color: var(--leaf);
  }
</style>
</head>
<body>
<main class="canvas">

  <section class="card card--front" aria-label="Business card front">
    <div class="front__brand">TQ Vitality</div>
    <div class="front__rule"></div>
    <div class="front__tab">WWW.TQVITALITY.COM</div>
  </section>

  <section class="card card--back" aria-label="Business card back">
    <svg class="back__art" viewBox="0 0 560 320" role="img" aria-label="Green and charcoal curved band with soft leaf texture">
      <path d="M0,0 H185 C118,120 205,262 430,320 H0 Z" fill="var(--leaf)"/>
      <path d="M0,150 C70,250 210,300 380,320 H0 Z" fill="var(--leaf-light)"/>
      <path d="M0,168 C70,262 200,304 350,320 H0 Z" fill="var(--charcoal)"/>
    </svg>

    <div class="back__name">YOUR NAME</div>
    <div class="back__title">Job Title</div>
    <div class="back__rule"></div>

    <ul class="contact">
      <li class="contact__item">
        <svg class="contact__icon" viewBox="0 0 16 16"><circle cx="8" cy="8" r="8" fill="var(--leaf)"/><path d="M5.2 4.3l1.4 1.6-.8 1c.5 1.1 1.2 1.8 2.3 2.3l1-.8 1.6 1.4-.9 1.4C7.2 11 5 8.8 4.8 5.2z" fill="#fff"/></svg>
        <span>000 000 0000</span>
      </li>
      <li class="contact__item">
        <svg class="contact__icon" viewBox="0 0 16 16"><circle cx="8" cy="8" r="8" fill="var(--leaf)"/><rect x="4" y="5.2" width="8" height="5.6" fill="#fff"/><path d="M4 5.4l4 3 4-3" fill="none" stroke="var(--leaf)" stroke-width="1"/></svg>
        <span>youremail@xyz.com</span>
      </li>
      <li class="contact__item">
        <svg class="contact__icon" viewBox="0 0 16 16"><circle cx="8" cy="8" r="8" fill="var(--leaf)"/><g fill="none" stroke="#fff" stroke-width="1"><circle cx="8" cy="8" r="4.2"/><ellipse cx="8" cy="8" rx="1.8" ry="4.2"/><path d="M3.8 8h8.4"/></g></svg>
        <span>www.tqvitality.com</span>
      </li>
    </ul>

    <div class="back__brand">TQ Vitality</div>
  </section>

</main>
</body>
</html>
```